Email PDF Guide for Quellbrook

We are an online professional services website which helps start ups and small businesses gain access to the R&D tax incentive.

We want to educate businesses across multiple industries to understand what they need to do to access this tax incentive, with information relevant to their industry. We need a designer to pull together and design images and relevant visuals for a downloadable guide. Please note - we will provide all the content for this, your job is to pull this into a stylised guide, which is inviting to our audience and compliment the words with imagery.

We are looking to produce 12 guides in total but will start with one to confirm design and style. Then follow up with remaining 11 industries.

First industry: Technology and Software

To get a sense for what we do our site is: https://www.quellbrook.example/

Very interested to hear what the community comes up with to create something visually engaging and relevant to our site and message.

Target Market(s)

Start up founders and entrepreneurs in technology industry. Average age 35.

Industry/Entity Type

Information Technology

Font styles to use
Other font styles liked:
• Proxima Nova

Requirements
Must have
• - Guide needs to be minimum of 8 pages, content currently totals 5 word pages.
• - The format needs to be editable on standard Google or Microsoft products then formatted into PDF, so we can make text changes at later dates (can discuss this criteria if difficult)
• - Font is Proxima Nova
• - Colours and gradients can be found here: http://tandivelle.example.com/
• - Colour selection should be:
• * Main palette = #ff7c14 , #ffa800 , #fc4e78
• * Gray palette = #cccccc , #c1d1d9 , #f5f7f9 , #080808 , #2d3338 , #666666 , #6f7c82 , #999999
Nice to have
• Play with the title for best design format.
• Happy with one of the following options:
• - R&D in the Technology Industry
• - What you need to know about R&D in Technologu

```html
<!DOCTYPE html>
<html lang="en">
<head>
<meta charset="utf-8">
<title>R&amp;D in the Technology Industry – Quellbrook Guide</title>
<link rel="stylesheet" href="https://fonts.googleapis.com/css2?family=Source+Sans+3:wght@300;400;600&display=swap">
<style>
  :root{
    --orange:#ff7c14;
    --orange-soft:#ffb066;
    --orange-pale:#fde3cc;
    --orange-mist:#fff4ea;
    --grey-text:#2d3338;
    --grey-mid:#666666;
    --stage:#1d1c1b;
    --board:#ffffff;
    --page-border:#bdbdbd;
  }
  *{box-sizing:border-box;margin:0;padding:0}
  html,body{width:1200px;height:1000px;overflow:hidden;background:var(--stage)}
  body{font-family:"Source Sans 3",sans-serif;color:var(--grey-text);position:relative}
  .board{position:absolute;left:8px;top:57px;width:1184px;height:819px;background:var(--board)}
  .page{position:absolute;width:284px;height:400px;background:#fff;border:1px solid var(--page-border);overflow:hidden}
  .page-heading{color:var(--orange);font-weight:400;font-size:13.5px;line-height:1.2;margin:0 0 10px}
  .page-body{position:absolute;left:18px;right:16px;top:26px;font-size:7.3px;line-height:9.3px}
  .page-body p{margin-bottom:9px}
  .page-body ul{list-style:none;margin-bottom:9px}
  .page-body li{padding-left:17px;position:relative}
  .page-body li::before{content:"•";position:absolute;left:0}
  .page-body h4{font-size:7.3px;font-weight:600;margin-bottom:9px}
  .page-number{position:absolute;right:18px;bottom:8px;font-size:7.5px;color:var(--grey-text)}
  .page-footer{position:absolute;left:0;bottom:0;width:100%;height:40px;
    background:linear-gradient(180deg,rgba(255,255,255,0) 0%,var(--orange-mist) 35%,var(--orange-pale) 100%)}
  .page-art{position:absolute;left:0;bottom:0;width:100%;height:148px;
    background:linear-gradient(180deg,var(--orange-mist) 0%,var(--orange-pale) 28%,var(--orange-soft) 100%)}
  .brand{position:absolute;left:14px;top:24px;display:flex;align-items:center;gap:6px}
  .brand-mark{width:8px;height:8px;background:var(--orange)}
  .brand-name{font-size:12px;font-weight:600;color:var(--grey-text)}
  .brand-product{font-size:12px;color:var(--grey-mid);margin-left:10px}
  .cover-title{position:absolute;left:0;right:0;top:96px;text-align:center;color:var(--orange);font-weight:400;font-size:23px;line-height:1.22}
  .cover-byline{position:absolute;left:0;right:0;top:157px;text-align:center;font-size:7.5px;font-weight:600}
  .cover-volume{position:absolute;right:36px;top:166px;font-size:122px;font-weight:400;line-height:1;background:linear-gradient(#c4c4c4,#8c8c8c);-webkit-background-clip:text;background-clip:text;color:transparent}
  .contents-heading{position:absolute;left:18px;top:84px;color:var(--orange);font-size:18px;font-weight:400}
  .contents-list{position:absolute;left:18px;top:108px;list-style:none;font-size:9px;line-height:11.4px}
  .contact{position:absolute;left:0;right:0;top:152px;text-align:center;color:var(--orange);font-size:9px;line-height:1.25}
</style>
</head>
<body>
<div class="board">

  <section class="page page--cover" style="left:12px;top:5px">
    <div class="brand"><span class="brand-mark"></span><span class="brand-name">Marrowby</span><span class="brand-product">Quell R&amp;D</span></div>
    <h1 class="cover-title">R&amp;D<br>in the Technology Industry</h1>
    <p class="cover-byline">By: Quellbrook</p>
    <div class="cover-volume">1</div>
    <div class="page-art" role="img" aria-label="Abstract decorative artwork in orange and grey tones"></div>
  </section>

  <section class="page" style="left:305px;top:5px">
    <h2 class="contents-heading">Content</h2>
    <ul class="contents-list">
      <li>H1: Introduction</li>
      <li>H2: Summary of R&amp;D Tax Incentive</li>
      <li>H3: What is R&amp;D?</li>
      <li>H4: Benefits of conducting R&amp;D activities</li>
      <li>H5: Eligibility to claim the R&amp;D Tax Incentive</li>
      <li>H6: Claiming the R&amp;D Tax Incentive in the Technology sector</li>
      <li>H7: Registration of R&amp;D activities</li>
      <li>H8: Applying for the R&amp;D Tax Incentive</li>
    </ul>
    <div class="page-footer" role="img" aria-label="Soft orange decorative footer band"></div>
  </section>

  <section class="page" style="left:599px;top:5px">
    <div class="page-body" style="top:31px">
      <h2 class="page-heading" style="margin-bottom:18px">H1: Introduction</h2>
      <p>The technology industry is always evolving. Businesses and startups within the industry seek to innovate and take part in Research &amp; Development projects (R&amp;D) to stay ahead.</p>
      <p>If your tech company works on innovative projects, you may be eligible for a tax offset under the R&amp;D Tax Incentive.</p>
    </div>
    <div class="page-footer" role="img" aria-label="Soft orange decorative footer band"></div>
    <span class="page-number">1</span>
  </section>

  <section class="page" style="left:890px;top:5px">
    <div class="page-body" style="top:22px">
      <h2 class="page-heading" style="margin-bottom:6px">H2: Summary of R&amp;D Tax Incentive</h2>
      <p>The Australian government supports innovation by encouraging local businesses to develop new or improved products and original solutions. This support is offered through the Research &amp; Development (R&amp;D) Tax Incentive, reducing the financial risk involved in undertaking R&amp;D activities. By reducing the risks and costs associated with conducting R&amp;D, the incentive seeks to boost productivity, innovation and economic growth for the nation.</p>
      <p>The R&amp;D Tax Incentive offers a targeted tax offset of up to a 45% refund of costs for eligible Research &amp; Development activities that benefit Australia.</p>
      <p>Many businesses in Australia are already completing eligible R&amp;D activities without realising. In fact, only 30% of eligible small businesses conducting R&amp;D currently claim this tax incentive. You don't need to be conducting experiments in a lab to qualify for R&amp;D incentives. If your business prides itself on innovation or is considering new developments, read on to find out more about how the R&amp;D Tax Incentive could provide cash back to your company.</p>
    </div>
    <span class="page-number">2</span>
  </section>

  <section class="page" style="left:12px;top:414px">
    <div class="page-body" style="top:28px">
      <h2 class="page-heading" style="margin-bottom:7px">H3: What is R&amp;D?</h2>
      <p>Research &amp; Development, or R&amp;D, involves conducting an experiment or trial to gain new knowledge. This new knowledge could be used to develop new or improved materials, products, devices, processes, software, or services. An experiment doesn't have to be scientific, all it means it that at the start of this process you're unaware of what the outcome will be and need to conduct further research, testing and trialling in order to overcome this uncertainty. The results seek to bridge the gap in knowledge that you started with.</p>
      <p>A wide range of businesses and industries conduct R&amp;D activities including (but not limited to):</p>
      <ul><li>Professional services</li><li>Manufacturing</li><li>Agriculture</li><li>Retail</li><li>Fashion</li><li>Science</li><li>Technology</li></ul>
    </div>
    <div class="page-footer" role="img" aria-label="Soft orange decorative footer band"></div>
    <span class="page-number">3</span>
  </section>

  <section class="page" style="left:305px;top:414px">
    <div class="page-body" style="top:28px">
      <h2 class="page-heading" style="margin-bottom:7px">H4: Benefits of conducting R&amp;D activities</h2>
      <p>Research and Development helps to improve workforce skills and knowledge, venture capital opportunities, and technical proficiencies within a business. Innovation and cutting-edge solutions not only puts your company at the forefront of competition, it also supports the development of the Australian workforce and economy.</p>
      <h4>Financial benefits of R&amp;D Tax Incentive</h4>
      <p>Undertaking R&amp;D involves significant technical and financial risk. The R&amp;D Tax Incentive was introduced to encourage businesses in Australia to take on R&amp;D activities. Unlike a grant, you are not applying for funding or competing with other businesses for this financial incentive. Instead, the financial benefit is received in the way of tax offsets against expenses and is available to all eligible businesses.</p>
      <p>Small businesses (turnover below $20 million) can receive a 45% R&amp;D tax offset against expenses in a financial year. Larger companies (over $20 million aggregated turnover) can receive a 40% R&amp;D tax offset.</p>
      <p>Companies that have experienced a tax loss can also benefit from the R&amp;D Tax Incentive and could be eligible to offset 45cents for every dollar spent on R&amp;D activities.</p>
    </div>
    <div class="page-footer" role="img" aria-label="Soft orange decorative footer band"></div>
    <span class="page-number">4</span>
  </section>

  <section class="page" style="left:599px;top:414px">
    <div class="page-body" style="top:19px">
      <h2 class="page-heading" style="margin-bottom:6px">H5: Eligibility to claim the R&amp;D Tax Incentive</h2>
      <p>More than 20,000 small businesses are currently eligible for the R&amp;D Tax Incentive, yet only 7,000 currently apply for this program.</p>
      <p>When you hear R&amp;D, you might be thinking of large corporations developing new products in laboratories. This is a common misconception, but almost every type of business conducts R&amp;D in one form of another, regardless of their size or industry.</p>
      <p>Your business is likely to be eligible if it is:</p>
      <ul><li>Incorporated as a company</li><li>A for-profit entity</li><li>Registered in Australia</li><li>Spent more than $20,000 on eligible R&amp;D expenses</li></ul>
      <p>However, you are not eligible to apply your business is:</p>
      <ul><li>An individual sole trader</li><li>A corporate limited partnership</li><li>An exempt entity (where your entire income is exempt from income tax).</li></ul>
      <p>Your business can only benefit from the program if your initiatives are considered eligible R&amp;D activities and meet the legal requirements. This is to ensure that companies do not take advantage of the program solely for the purpose of gaining additional income.</p>
    </div>
    <div class="page-footer" role="img" aria-label="Soft orange decorative footer band"></div>
    <span class="page-number">5</span>
  </section>

  <section class="page" style="left:890px;top:414px">
    <p class="contact">Quellbrook<br>Email: support@quellbrook.example<br>Phone: 1800 555 014</p>
    <div class="page-art" role="img" aria-label="Abstract decorative artwork in orange and grey tones"></div>
  </section>

</div>
</body>
</html>
```